Ashby Meadows Thank-You Tag

Looking for a file that incorporates current branding/colors and says:

"Thanks for Swimming with Us!"
Ashby Meadows Otters

Samples of other pieces we've done recently are attached.

Will be printed on cardstock that is
Width: 3.5 inches
Height: 2.5 inches

```html
<!DOCTYPE html>
<html lang="en">
<head>
<meta charset="utf-8">
<title>Ashby Meadows Thank-You Tag</title>
<link rel="stylesheet" href="https://fonts.googleapis.com/css2?family=Londrina+Solid:wght@900&family=Poppins:wght@600;700&display=swap">
<style>
  :root {
    --backdrop: #b7b7b7;
    --card: #ffffff;
    --navy: #2b4fa0;
    --pink: #ee5f9f;
    --sky: #8bbce6;
    --silver: #c9ced6;
    --blush: #f6b3d1;
    --skytint: #c2dcf3;
  }
  html, body {
    margin: 0;
    width: 1200px;
    height: 907px;
    overflow: hidden;
    background: var(--backdrop);
  }
  .tag { display: block; width: 1200px; height: 907px; }
  .year { font-family: "Poppins", sans-serif; font-weight: 700; }
  .year-top { fill: var(--navy); }
  .year-bottom { fill: var(--pink); }
  .year-ring { fill: none; stroke: var(--navy); stroke-width: 17; }
  .club-name { font-family: "Poppins", sans-serif; font-weight: 700; font-size: 11px; fill: var(--navy); letter-spacing: 0.5px; }
  .message { font-family: "Londrina Solid", sans-serif; font-weight: 900; }
  .message-navy { fill: var(--navy); }
  .message-pink { fill: var(--pink); }
  .wave-sky { fill: none; stroke: var(--sky); stroke-width: 36; }
  .wave-pink { fill: var(--pink); }
</style>
</head>
<body>
<svg class="tag" viewBox="0 0 1200 907" xmlns="http://www.w3.org/2000/svg" aria-labelledby="tag-title">
  <title id="tag-title">Ashby Meadows Otters – Thanks for swimming with us! 2026</title>
  <defs>
    <clipPath id="card-clip"><rect x="113" y="104" width="975" height="697"/></clipPath>
  </defs>

  <rect class="card" x="113" y="104" width="975" height="697" fill="var(--card)"/>

  <g clip-path="url(#card-clip)">
    <!-- Season year -->
    <g class="season-year">
      <text class="year year-top" x="172" y="294" font-size="160">2</text>
      <circle class="year-ring" cx="338" cy="237" r="50"/>
      <text class="club-name" x="338" y="234" text-anchor="middle">ASHBY</text>
      <text class="club-name" x="338" y="249" text-anchor="middle">MEADOWS</text>
      <text class="year year-bottom" x="206" y="438" font-size="178" letter-spacing="-8">26</text>
    </g>

    <!-- Illustration areas -->
    <rect role="img" aria-label="Silver leaping dolphin illustration" x="780" y="172" width="108" height="118" rx="40" fill="var(--silver)"/>
    <rect role="img" aria-label="Pink water splash illustration" x="790" y="244" width="84" height="80" rx="36" fill="var(--blush)"/>
    <rect role="img" aria-label="Light blue dolphin leaping from the waves illustration" x="234" y="466" width="172" height="176" rx="70" fill="var(--skytint)"/>
    <rect role="img" aria-label="Blue water splash illustration" x="736" y="552" width="114" height="96" rx="40" fill="var(--skytint)"/>

    <!-- Message -->
    <g class="message-block">
      <text class="message message-navy" x="484" y="408" font-size="104" textLength="518" lengthAdjust="spacingAndGlyphs">THANKS FOR</text>
      <text class="message message-pink" x="423" y="513" font-size="150" textLength="589" lengthAdjust="spacingAndGlyphs">SWIMMING</text>
      <text class="message message-navy" x="423" y="600" font-size="104" textLength="351" lengthAdjust="spacingAndGlyphs">WITH US!</text>
    </g>

    <!-- Waves -->
    <path class="wave-sky" d="M100 688 Q150 668 200 676 T300 676 T400 680 T500 676 T600 680 T700 676 T800 680 T900 676 T1000 680 T1100 672"/>
    <path class="wave-pink" d="M100 736 Q150 712 200 722 T300 722 T400 726 T500 720 T600 726 T700 720 T800 726 T900 720 T1000 726 T1100 716 L1100 810 L100 810 Z"/>
  </g>
</svg>
</body>
</html>
```